Business Card Design Project

I have had my current business card for 6years and it is time to upgrade my business card. I have uploaded my old card
I am a retail specialty shop designer and want something designer looking but professional.
Target Market(s)
30-60 year old people in retail businesses
Industry/Entity Type
Retail
Requirements
Must have
- The Vela Fitouts logo (but colour can and style can be altered)
My name, position and contact details as per my existing card attached .
Rupert Calloway Director
m: 0418536771
rupert@velafitouts.com.au
www.velafitouts.com.au
t:02 94417268 f: 02 94417293
po box 817 alexandria nsw 1435
Nice to have
- Use both sides of the card

```html
<!DOCTYPE html>
<html lang="en">
<head>
<meta charset="utf-8">
<title>Vela Fitouts — Business Card</title>
<link rel="stylesheet" href="https://fonts.googleapis.com/css2?family=Jura:wght@400;500;600&display=swap">
<style>
  :root {
    --bg: #e9e6e1;
    --card: #141414;
    --card-edge: #1f1f1f;
    --ink: #f2f2f2;
    --ink-soft: #bdbdbd;
    --band: #5c5c5c;
    --rule: #8a8a8a;
  }
  * { box-sizing: border-box; margin: 0; padding: 0; }
  html, body {
    width: 1200px; height: 960px; overflow: hidden;
    background: var(--bg);
    font-family: "Jura", sans-serif;
    color: var(--ink);
  }
  .stage { position: relative; width: 1200px; height: 960px; }
  .card {
    position: absolute;
    width: 740px; height: 424px;
    background: radial-gradient(ellipse at 30% 20%, #1d1d1d 0%, var(--card) 70%);
    border: 1px solid var(--card-edge);
    box-shadow: 0 6px 18px rgba(0,0,0,0.25);
  }
  .card--front { left: 120px; top: 40px; }
  .card--back  { left: 340px; top: 496px; }

  .brand {
    position: absolute; left: 40px; top: 38px;
    display: flex; align-items: center; gap: 12px;
  }
  .brand__mark { width: 22px; height: 22px; background: var(--ink); }
  .brand__name {
    font-size: 26px; font-weight: 500; letter-spacing: 1px;
    text-transform: uppercase; color: var(--ink);
  }

  .identity { position: absolute; left: 0; right: 0; top: 170px; text-align: center; }
  .identity__name { font-size: 40px; font-weight: 500; }
  .identity__rule { width: 320px; height: 2px; background: var(--rule); margin: 10px auto 14px; }
  .identity__role { font-size: 26px; font-weight: 500; }

  .contact-line {
    position: absolute; bottom: 26px; font-size: 20px; font-weight: 500;
    display: flex; align-items: center; gap: 8px;
  }
  .contact-line--mobile { left: 34px; }
  .contact-line--phone { right: 34px; }
  .icon { width: 18px; height: 22px; flex: none; }

  .tagline-band {
    position: absolute; left: 0; right: 0; top: 170px; height: 64px;
    background: var(--band);
    display: flex; align-items: center; justify-content: flex-end;
    padding-right: 70px;
  }
  .tagline { font-size: 38px; font-weight: 500; letter-spacing: 1px; }

  .details {
    position: absolute; top: 290px; font-size: 17px; font-weight: 500;
    color: var(--ink-soft); display: flex; flex-direction: column; gap: 26px;
  }
  .details--left { left: 70px; }
  .details--right { left: 450px; }
  .details__item { display: flex; align-items: center; gap: 12px; white-space: nowrap; }
  .details__item .icon { width: 20px; height: 16px; }
</style>
</head>
<body>
<main class="stage">

  <section class="card card--front" aria-label="Card front">
    <div class="brand">
      <span class="brand__mark"></span>
      <span class="brand__name">Vela Fitouts</span>
    </div>
    <div class="identity">
      <h1 class="identity__name">Rupert Calloway</h1>
      <div class="identity__rule"></div>
      <p class="identity__role">Director</p>
    </div>
    <p class="contact-line contact-line--mobile">m: 0418 536 771</p>
    <p class="contact-line contact-line--phone">
      <svg class="icon" viewBox="0 0 18 22" aria-hidden="true">
        <rect x="3" y="1" width="12" height="20" rx="2" fill="none" stroke="#f2f2f2" stroke-width="2"/>
        <rect x="6" y="5" width="6" height="5" fill="#f2f2f2"/>
      </svg>
      (02) 9441 7268
    </p>
  </section>

  <section class="card card--back" aria-label="Card back">
    <div class="brand">
      <span class="brand__mark"></span>
      <span class="brand__name">Vela Fitouts</span>
    </div>
    <div class="tagline-band">
      <p class="tagline">Let's get it done</p>
    </div>
    <div class="details details--left">
      <p class="details__item">
        <svg class="icon" viewBox="0 0 20 16" aria-hidden="true">
          <rect x="1" y="1" width="18" height="14" fill="none" stroke="#bdbdbd" stroke-width="2"/>
          <polyline points="1,1 10,9 19,1" fill="none" stroke="#bdbdbd" stroke-width="2"/>
        </svg>
        rupert@velafitouts.com.au
      </p>
      <p class="details__item">
        <svg class="icon" viewBox="0 0 20 16" aria-hidden="true">
          <polygon points="10,0 20,8 17,8 17,16 3,16 3,8 0,8" fill="#bdbdbd"/>
        </svg>
        www.velafitouts.com.au
      </p>
    </div>
    <div class="details details--right">
      <p class="details__item">FAX 02 9441 7293</p>
      <p class="details__item">po box 817 harbourleigh nsw 2199</p>
    </div>
  </section>

</main>
</body>
</html>
```